Velvet Harbor Powerpoint Presentation

Looking for powerpoint presentation template for our boutique social media management and digital marketing company.
We will be using this Powerpoint template for presentations, guest speaking sessions and proposals.
We need a front page and then a few different versions of what the rest of the template would look like.
I have attached our business cards, different versions of our logo, and our PDF so you can get a look at our identity and get a feel of what we are about. Our website will be up in about two weeks.
Target Market(s)
Small to medium size business owners (all different catagories)
Industry/Entity Type
Marketing
Requirements
Must have
- The logo
- a very boutique, high end look. You will see what I mean when you look at our business cards and our PDF.
- We only want to use the Velvet Harbor colors- Black, White, Rose Gold and Grey
Should not have
- Lot's of colors that are not part of the Velvet Harbor identity

```html
<!DOCTYPE html>
<html lang="en">
<head>
<meta charset="utf-8">
<title>Velvet Harbor Presentation Template</title>
<link href="https://fonts.googleapis.com/css2?family=Roboto:wght@300;400;500&display=swap" rel="stylesheet">
<style>
:root{
  --ink:#1c1c1c;
  --char:#2b2b2b;
  --rose:#f2d8cd;
  --rose-deep:#e6c3b5;
  --grey:#6b6b6b;
  --silver:#a9a9a9;
  --mist:#f3f3f3;
  --paper:#ffffff;
  --text:#333333;
  --faint:#a6a6a6;
}
*{box-sizing:border-box;margin:0;padding:0}
html,body{width:1029px;height:1200px;overflow:hidden;background:var(--paper)}
body{font-family:'Roboto',sans-serif;font-weight:300;color:var(--text)}
.deck{display:grid;grid-template-columns:repeat(3,337px);grid-auto-rows:189px;gap:10px 6px;padding:8px 3px}
.slide{position:relative;overflow:hidden;background:var(--paper);box-shadow:0 0 0 .5px #dcdcdc}
.abs{position:absolute}
.title{position:absolute;left:14px;top:14px;font-size:14px;font-weight:300;letter-spacing:.3px;color:var(--ink);line-height:1.1}
.title::after{content:'';position:absolute;left:0;bottom:-4px;width:14px;height:1px;background:var(--rose-deep)}
.brand{position:absolute;right:9px;top:8px;display:flex;flex-direction:column;align-items:center;font-size:5.6px;letter-spacing:.2px;color:#555;font-weight:400}
.brand i{width:9px;height:9px;border:1px solid #777;border-radius:50%;margin-bottom:2px}
.brand.light{color:#999}
.brand.light i{border-color:#999}
.foot{position:absolute;left:0;right:0;bottom:0;height:9px;background:var(--ink);color:#bbb;font-size:3.6px;display:flex;justify-content:space-between;align-items:center;padding:0 5px;font-weight:400}
.tiny{font-size:4px;color:var(--faint);line-height:1.4}
.label{font-size:5.4px;color:var(--text);font-weight:400}
.dot{display:inline-block;border-radius:50%}
.item{position:absolute;display:flex;gap:4px;align-items:flex-start}
.item .dot{width:8px;height:8px;flex:none;margin-top:1px}
.photo{position:absolute;background:linear-gradient(135deg,#d8d8d8,#8a8a8a)}
.dark-photo{position:absolute;inset:0;background:linear-gradient(140deg,#3a3a3a,#151515 60%,#2d2d2d)}
.center{text-align:center}
/* pricing */
.plan{position:absolute;text-align:center}
.plan-head{display:flex;flex-direction:column;justify-content:center;align-items:center;color:#fff;font-size:13px}
.plan-head small{font-size:3.5px}
.plan-body{background:#fff;padding-top:4px}
.plan-body p{font-size:3.6px;color:#777;padding:3px 0;border-bottom:.5px solid #e2e2e2;margin:0 8px}
.plan-body p:last-child{border:0}
/* table */
.grid-table{position:absolute;left:22px;top:62px;width:292px;border-collapse:collapse;font-size:3.8px;text-align:center;font-weight:400}
.grid-table th{background:var(--ink);color:#fff;height:8px;font-weight:400}
.grid-table td{height:8px;color:#777;border-right:.5px solid #fff}
.grid-table tr:nth-child(even) td{background:var(--mist)}
.grid-table tr:nth-child(odd) td{background:#fafafa}
/* column boxes */
.colbox{position:absolute;top:72px;width:62px;height:82px;display:flex;flex-direction:column;align-items:center;padding-top:10px;color:#fff}
.colbox .ic{width:16px;height:16px;border-radius:50%;background:#fff;margin-bottom:12px}
.colbox .label{color:inherit;font-size:3.8px}
.colbox .tiny{color:inherit;opacity:.75;text-align:center;padding:0 6px}
</style>
</head>
<body>
<main class="deck">

<!-- 1 pie -->
<section class="slide">
  <h2 class="title">YOUR PIE CHART AREA</h2>
  <div class="brand"><i></i>VELVET HARBOR</div>
  <svg class="abs" style="left:40px;top:40px" width="130" height="80" viewBox="0 0 130 80">
    <path d="M5,30 L5,44 A60,24 0 0 0 125,44 L125,30 A60,24 0 0 1 5,30Z" fill="#0f0f0f"/>
    <path d="M5,30 A60,24 0 0 0 30,49.5 L30,63.5 A60,24 0 0 1 5,44Z" fill="#d9b8ab"/>
    <ellipse cx="65" cy="30" rx="60" ry="24" fill="#1c1c1c"/>
    <path d="M65,30 L5,30 A60,24 0 0 0 30,49.5Z" fill="#f2d8cd"/>
    <path d="M65,30 L5,30 A60,24 0 0 1 50,6.8Z" fill="#6b6b6b"/>
    <text x="52" y="76" font-size="3.5" fill="#999">● Series A  ● Series B  ● Series C</text>
  </svg>
  <div class="item" style="left:212px;top:56px"><span class="dot" style="background:var(--ink)"></span><div><div class="label">Your Text Here</div><div class="tiny">Lorem ipsum dolor sit amet.</div></div></div>
  <div class="item" style="left:212px;top:80px"><span class="dot" style="background:var(--grey)"></span><div><div class="label">Your Text Here</div><div class="tiny">Lorem ipsum dolor sit amet.</div></div></div>
  <div class="item" style="left:212px;top:104px"><span class="dot" style="background:var(--silver)"></span><div><div class="label" style="color:#aaa">Your Text Here</div><div class="tiny">Lorem ipsum dolor sit amet.</div></div></div>
  <svg class="abs" style="left:22px;top:141px" width="10" height="9"><path d="M5,0 L10,9 L0,9Z" fill="#f2d8cd"/></svg>
  <div class="abs" style="left:35px;top:138px;font-size:12px">54%</div>
  <div class="abs" style="left:70px;top:138px;width:220px"><div class="label">Heading Goes Here</div><div class="tiny">Lorem ipsum dolor sit amet, consectetur adipiscing elit, sed do eiusmod tempor incididunt ut labore et dolore magna aliqua. Ut enim ad minim veniam, quis nostrud exercitation ullamco laboris nisi ut aliquip ex ea commodo consequat.</div></div>
  <div class="foot"><span>© 2017 VELVET HARBOR. All rights reserved.</span><span>34</span></div>
</section>

<!-- 2 line charts -->
<section class="slide">
  <h2 class="title">YOUR LINE CHART AREA</h2>
  <div class="brand"><i></i>VELVET HARBOR</div>
  <svg class="abs" style="left:30px;top:62px" width="290" height="80" viewBox="0 0 290 80">
    <g font-size="4" fill="#999">
      <text x="42" y="8">Chart Title</text><text x="200" y="8">Chart Title</text>
      <text x="2" y="18">70</text><text x="2" y="32">50</text><text x="2" y="46">30</text><text x="2" y="60">10</text>
      <text x="162" y="18">70</text><text x="162" y="32">50</text><text x="162" y="46">30</text><text x="162" y="60">10</text>
      <text x="20" y="72">a   b   c   d   e</text><text x="180" y="72">a   b   c   d   e</text>
    </g>
    <polyline points="14,58 30,26 46,62 62,38 78,24 94,48" fill="none" stroke="#1c1c1c" stroke-width="1.2"/>
    <polyline points="14,40 30,30 46,50 62,32 78,44 94,36" fill="none" stroke="#a9a9a9" stroke-width="1"/>
    <polyline points="174,58 190,26 206,62 222,38 238,24 254,48" fill="none" stroke="#1c1c1c" stroke-width="1.2"/>
    <polyline points="174,40 190,30 206,50 222,32 238,44 254,36" fill="none" stroke="#a9a9a9" stroke-width="1"/>
  </svg>
  <div class="tiny abs" style="left:36px;top:144px;width:116px">Lorem ipsum dolor sit amet consectetur adipiscing elit sed diam nonummy nibh euismod tempor ut labore.</div>
  <div class="tiny abs" style="left:194px;top:144px;width:116px">Lorem ipsum dolor sit amet consectetur adipiscing elit sed diam nonummy nibh euismod tempor ut labore.</div>
  <div class="foot"><span>© 2017 VELVET HARBOR. All rights reserved.</span><span>35</span></div>
</section>

<!-- 3 line chart slide -->
<section class="slide">
  <div class="brand"><i></i>VELVET HARBOR</div>
  <div class="abs" style="left:22px;top:42px;font-size:14px;line-height:1.3;color:var(--ink)">THIS IS LINE<br>CHART SLIDE</div>
  <div class="abs" style="left:24px;top:88px;width:76px;height:10px;background:var(--ink);color:#fff;font-size:4px;display:flex;align-items:center;justify-content:center;font-weight:400">CREATIVE TEXT HERE</div>
  <div class="tiny abs" style="left:28px;top:112px;width:82px"><span style="color:#333">Lorem ipsum dolor</span> sit amet, consectetur adipiscing elit, sed do eiusmod tempor incididunt ut labore et commodo consequat dolore magna aliqua.</div>
  <svg class="abs" style="left:134px;top:46px" width="195" height="120" viewBox="0 0 195 120">
    <g font-size="4" fill="#999">
      <text x="0" y="6">5</text><text x="0" y="21">4.5</text><text x="0" y="36">3.5</text><text x="0" y="51">3</text><text x="0" y="66">2.5</text><text x="0" y="81">1.5</text><text x="0" y="96">0.5</text><text x="0" y="111">0</text>
      <text x="20" y="118">Category 1</text><text x="64" y="118">Category 2</text><text x="108" y="118">Category 3</text><text x="152" y="118">Category 4</text>
    </g>
    <polyline points="30,22 75,70 118,55 162,30" fill="none" stroke="#1c1c1c" stroke-width="1.4"/>
    <polyline points="30,72 75,20 118,82 162,60" fill="none" stroke="#8a8a8a" stroke-width="1.4"/>
    <g fill="#1c1c1c"><circle cx="30" cy="22" r="1.6"/><circle cx="75" cy="70" r="1.6"/><circle cx="118" cy="55" r="1.6"/><circle cx="162" cy="30" r="1.6"/></g>
    <g fill="#8a8a8a"><circle cx="30" cy="72" r="1.6"/><circle cx="75" cy="20" r="1.6"/><circle cx="118" cy="82" r="1.6"/><circle cx="162" cy="60" r="1.6"/></g>
  </svg>
  <div class="foot"><span>© 2017 VELVET HARBOR. All rights reserved.</span><span>36</span></div>
</section>

<!-- 4 table -->
<section class="slide">
  <h2 class="title">YOUR TABLE AREA</h2>
  <div class="brand"><i></i>VELVET HARBOR</div>
  <div class="tiny abs" style="left:22px;top:44px;width:200px"><span style="color:#333">Description:</span> Lorem ipsum dolor sit amet, a short passage of sample text to set the table.</div>
  <table class="grid-table">
    <tr><th>Lorem ipsum</th><th>Value</th><th>Value</th><th>Value</th><th>Value</th></tr>
    <tr><td>Lorem ipsum</td><td>10</td><td>15</td><td>16</td><td>15</td></tr>
    <tr><td>Lorem ipsum</td><td>12</td><td>13</td><td>15</td><td>16</td></tr>
    <tr><td>Lorem ipsum</td><td>20</td><td>22</td><td>21</td><td>21</td></tr>
    <tr><td>Lorem ipsum</td><td>10</td><td>21</td><td>12</td><td>11</td></tr>
    <tr><td>Lorem ipsum</td><td>25</td><td>25</td><td>25</td><td>25</td></tr>
    <tr><td>Lorem ipsum</td><td>10</td><td>02</td><td>51</td><td>21</td></tr>
    <tr><td>Lorem ipsum</td><td>35</td><td>36</td><td>65</td><td>32</td></tr>
    <tr><td>Lorem ipsum</td><td>26</td><td>33</td><td>65</td><td>32</td></tr>
    <tr><td>Lorem ipsum</td><td>32</td><td>10</td><td>32</td><td>32</td></tr>
  </table>
  <div class="foot"><span>© 2017 VELVET HARBOR. All rights reserved.</span><span>37</span></div>
</section>

<!-- 5 subscription -->
<section class="slide">
  <h2 class="title">MONTHLY SUBSCRIPTION</h2>
  <div class="brand"><i></i>VELVET HARBOR</div>
  <div class="abs" style="left:0;right:0;top:96px;bottom:0;background:var(--ink)"></div>
  <div class="plan" style="left:50px;top:63px;width:68px">
    <div class="plan-head" style="background:var(--grey);height:30px">$300<small>per month</small></div>
    <div class="plan-body" style="height:62px"><p>Single Edition</p><p>30gb Cloud Service</p><p>3 User</p><p>Free Update</p></div>
  </div>
  <div class="plan" style="left:126px;top:58px;width:86px">
    <div class="plan-head" style="background:var(--ink);height:35px;font-size:15px">$900<small>per month</small></div>
    <div class="plan-body" style="height:70px"><p>Business Edition</p><p>60gb Cloud Service</p><p>6 User</p><p>Free Update</p></div>
  </div>
  <div class="plan" style="left:220px;top:63px;width:68px">
    <div class="plan-head" style="background:var(--rose);height:30px;color:#777">$400<small>per month</small></div>
    <div class="plan-body" style="height:62px"><p>Single Edition</p><p>30gb Cloud Service</p><p>3 User</p><p>Free Update</p></div>
  </div>
</section>

<!-- 6 divider -->
<section class="slide">
  <div class="dark-photo" role="img" aria-label="Dark monochrome photo of city towers seen from below"></div>
  <div class="brand light" style="top:20px;right:22px;font-size:8px"><i style="width:13px;height:13px"></i>VELVET HARBOR</div>
  <div class="abs center" style="left:0;width:270px;top:114px;color:#ddd">
    <div style="font-size:5px">Divider Page</div>
    <div style="font-size:14px;color:#fff">YOUR TITLE GOES HERE</div>
    <div style="font-size:7px;color:#bbb">Your Subtitle Here</div>
  </div>
</section>

<!-- 7 mockup -->
<section class="slide">
  <div class="abs" style="left:0;right:0;top:0;height:122px;background:var(--ink)"></div>
  <div class="brand light"><i></i>VELVET HARBOR</div>
  <div class="abs" style="left:16px;top:44px;font-size:16px;color:#fff;text-align:right;line-height:1.25;width:86px">OUR MOCK<br>UP AREA</div>
  <div class="abs" style="left:110px;top:30px;width:128px;height:92px;background:#bfbfbf;border-radius:4px;padding:4px">
    <div class="photo" style="inset:4px" role="img" aria-label="Monochrome city skyline on the laptop screen"></div>
  </div>
  <div class="abs" style="left:94px;top:122px;width:160px;height:5px;background:linear-gradient(#d9d9d9,#9a9a9a);border-radius:0 0 6px 6px"></div>
  <div class="item" style="left:20px;top:134px;flex-direction:row-reverse;text-align:right"><span class="dot" style="background:var(--grey)"></span><div><div class="label">Your Text Here</div><div class="tiny">Lorem ipsum dolor sit amet.</div></div></div>
  <div class="item" style="left:20px;top:158px;flex-direction:row-reverse;text-align:right"><span class="dot" style="background:var(--grey)"></span><div><div class="label">Your Text Here</div><div class="tiny">Lorem ipsum dolor sit amet.</div></div></div>
  <div class="item" style="left:240px;top:134px"><span class="dot" style="background:var(--ink)"></span><div><div class="label">Your Text Here</div><div class="tiny">Lorem ipsum dolor sit amet.</div></div></div>
  <div class="item" style="left:240px;top:158px"><span class="dot" style="background:var(--ink)"></span><div><div class="label">Your Text Here</div><div class="tiny">Lorem ipsum dolor sit amet.</div></div></div>
  <div class="foot"><span>© 2017 VELVET HARBOR. All rights reserved.</span><span>40</span></div>
</section>

<!-- 8 video -->
<section class="slide">
  <div class="brand"><i></i>VELVET HARBOR</div>
  <div class="abs" style="left:16px;top:28px;font-size:14px;line-height:1.05;color:var(--ink)">VIDEO TITLE<br>GOES HERE</div>
  <div class="tiny abs" style="left:16px;top:72px;width:82px">Lorem ipsum dolor sit amet consectetur adipiscing elit, sed do eiusmod tempor incididunt ut labore et commodo consequat dolore magna aliqua.<br><br>Duis aute irure dolor in reprehenderit in voluptate velit esse cillum dolore eu fugiat nulla pariatur.<br><br>Ut enim ad minim veniam, quis nostrud exercitation ullamco laboris.</div>
  <div class="abs" style="left:112px;top:30px;width:188px;height:118px;background:var(--ink);border-radius:4px;padding:5px 5px 14px">
    <div class="photo" style="inset:5px 5px 14px" role="img" aria-label="Monochrome photo of skyscrapers seen from below"></div>
  </div>
  <div class="abs" style="left:112px;top:139px;width:188px;height:9px;background:#d8d8d8;border-radius:0 0 4px 4px"></div>
  <div class="abs" style="left:196px;top:79px;width:22px;height:22px;border-radius:50%;background:#fff;opacity:.9"></div>
  <div class="abs" style="left:192px;top:148px;width:30px;height:14px;background:linear-gradient(#cfcfcf,#9d9d9d)"></div>
  <div class="abs" style="left:176px;top:161px;width:62px;height:3px;background:#bdbdbd;border-radius:2px"></div>
  <div class="foot"><span>© 2017 VELVET HARBOR. All rights reserved.</span><span>41</span></div>
</section>

<!-- 9 four column boxes -->
<section class="slide">
  <h2 class="title">FOUR COLUMN AREA</h2>
  <div class="brand"><i></i>VELVET HARBOR</div>
  <div class="tiny abs" style="left:26px;top:52px;width:290px">Lorem ipsum dolor sit amet, consectetur adipiscing elit, sed do eiusmod tempor incididunt ut labore et dolore magna aliqua. Ut enim ad minim veniam, quis nostrud exercitation ullamco laboris nisi ut aliquip ex ea commodo consequat.</div>
  <div class="colbox" style="left:26px;background:var(--ink)"><span class="ic"></span><div class="label">YOUR TEXT HERE</div><div class="tiny">Lorem ipsum dolor sit consectetur adipiscing elit.</div></div>
  <div class="colbox" style="left:100px;background:var(--rose)"><span class="ic"></span><div class="label">YOUR TEXT HERE</div><div class="tiny">Lorem ipsum dolor sit consectetur adipiscing elit.</div></div>
  <div class="colbox" style="left:174px;background:var(--grey)"><span class="ic"></span><div class="label">YOUR TEXT HERE</div><div class="tiny">Lorem ipsum dolor sit consectetur adipiscing elit.</div></div>
  <div class="colbox" style="left:249px;background:var(--silver)"><span class="ic"></span><div class="label">YOUR TEXT HERE</div><div class="tiny">Lorem ipsum dolor sit consectetur adipiscing elit.</div></div>
  <div class="foot"><span>© 2017 VELVET HARBOR. All rights reserved.</span><span>42</span></div>
</section>

<!-- 10 four column rings -->
<section class="slide">
  <h2 class="title">FOUR COLUMN AREA</h2>
  <div class="brand"><i></i>VELVET HARBOR</div>
  <div class="tiny abs" style="left:48px;top:42px;width:250px">Lorem ipsum dolor sit amet, consectetur adipiscing elit, sed do eiusmod tempor incididunt ut labore et dolore magna aliqua. Ut enim ad minim veniam, quis nostrud exercitation ullamco laboris.</div>
  <svg class="abs" style="left:0;top:0" width="337" height="189">
    <g fill="none" stroke-width="3">
      <circle cx="66" cy="86" r="19" stroke="#1c1c1c"/>
      <circle cx="134" cy="86" r="19" stroke="#f2d8cd"/>
      <circle cx="202" cy="86" r="19" stroke="#6b6b6b"/>
      <circle cx="270" cy="86" r="19" stroke="#c4c4c4"/>
    </g>
    <g font-size="5" text-anchor="middle" font-weight="400">
      <text x="66" y="117" fill="#333">COLUMN 1</text><text x="134" y="117" fill="#e2bfb1">COLUMN 2</text>
      <text x="202" y="117" fill="#333">COLUMN 3</text><text x="270" y="117" fill="#aaa">COLUMN 4</text>
    </g>
  </svg>
  <div class="tiny abs center" style="left:46px;top:122px;width:40px">Lorem ipsum dolor sit amet, sed do eiusmod tempor.</div>
  <div class="tiny abs center" style="left:114px;top:122px;width:40px">Lorem ipsum dolor sit amet, sed do eiusmod tempor.</div>
  <div class="tiny abs center" style="left:182px;top:122px;width:40px">Lorem ipsum dolor sit amet, sed do eiusmod tempor.</div>
  <div class="tiny abs center" style="left:250px;top:122px;width:40px">Lorem ipsum dolor sit amet, sed do eiusmod tempor.</div>
  <div class="foot"><span>© 2017 VELVET HARBOR. All rights reserved.</span><span>43</span></div>
</section>

<!-- 11 key points -->
<section class="slide">
  <h2 class="title">KEY POINTS AREA</h2>
  <div class="brand"><i></i>VELVET HARBOR</div>
  <div class="tiny abs" style="left:22px;top:56px;width:300px">Lorem ipsum dolor sit amet, consectetur adipiscing elit, sed do eiusmod tempor incididunt ut labore et dolore magna aliqua. Ut enim ad minim veniam, quis nostrud exercitation ullamco laboris.</div>
  <svg class="abs" style="left:0;top:0" width="337" height="189">
    <circle cx="87" cy="105" r="24" fill="#1c1c1c"/>
    <circle cx="128" cy="105" r="24" fill="#f2d8cd"/>
    <circle cx="168" cy="105" r="24" fill="#6b6b6b"/>
    <circle cx="209" cy="105" r="24" fill="#f2d8cd"/>
    <circle cx="249" cy="105" r="24" fill="#1c1c1c"/>
    <g font-size="4" text-anchor="middle">
      <text x="87" y="114" fill="#fff">Lorem ipsum</text><text x="128" y="114" fill="#b99">Lorem ipsum</text>
      <text x="168" y="114" fill="#fff">Lorem ipsum</text><text x="209" y="114" fill="#b99">Lorem ipsum</text>
      <text x="249" y="114" fill="#fff">Lorem ipsum</text>
    </g>
  </svg>
  <div class="tiny abs center" style="left:66px;top:140px;width:205px">Lorem ipsum dolor sit amet, consectetur adipiscing elit, sed do eiusmod tempor incididunt ut labore et dolore magna aliqua. Ut enim minim veniam, quis nostrud exercitation ullamco laboris.</div>
  <div class="foot"><span>© 2017 VELVET HARBOR. All rights reserved.</span><span>44</span></div>
</section>

<!-- 12 workflow -->
<section class="slide">
  <h2 class="title">WORKFLOW AREA</h2>
  <div class="brand"><i></i>VELVET HARBOR</div>
  <div class="tiny abs" style="left:26px;top:52px;width:294px">Lorem ipsum dolor sit amet, consectetur adipiscing elit, sed do eiusmod tempor incididunt ut labore et dolore magna aliqua. Ut enim minim veniam, quis nostrud exercitation ullamco.</div>
  <svg class="abs" style="left:0;top:0" width="337" height="189">
    <g fill="none" stroke-width="11">
      <path d="M26,106 A30,30 0 0 1 86,106" stroke="#1c1c1c"/>
      <path d="M86,106 A26,26 0 0 0 138,106" stroke="#f2d8cd"/>
      <path d="M138,106 A30,30 0 0 1 198,106" stroke="#1c1c1c"/>
      <path d="M198,106 A26,26 0 0 0 250,106" stroke="#f2d8cd"/>
      <path d="M250,106 A30,30 0 0 1 310,106" stroke="#1c1c1c"/>
    </g>
    <g font-size="4.5" text-anchor="middle">
      <circle cx="56" cy="96" r="5" fill="#1c1c1c"/><text x="56" y="98" fill="#fff">1</text>
      <circle cx="112" cy="120" r="5" fill="#f2d8cd"/><text x="112" y="122" fill="#b99">2</text>
      <circle cx="168" cy="96" r="5" fill="#1c1c1c"/><text x="168" y="98" fill="#fff">3</text>
      <circle cx="224" cy="120" r="5" fill="#f2d8cd"/><text x="224" y="122" fill="#b99">4</text>
      <circle cx="280" cy="96" r="5" fill="#1c1c1c"/><text x="280" y="98" fill="#fff">5</text>
      <text x="56" y="112" fill="#333">Data 1</text><text x="112" y="76" fill="#dbb">Data 2</text>
      <text x="168" y="112" fill="#333">Data 3</text><text x="224" y="76" fill="#dbb">Data 4</text>
      <text x="280" y="112" fill="#333">Data 5</text>
    </g>
  </svg>
  <div class="tiny abs center" style="left:38px;top:115px;width:36px">Lorem ipsum dolor sit amet.</div>
  <div class="tiny abs center" style="left:94px;top:80px;width:36px">Lorem ipsum dolor sit amet.</div>
  <div class="tiny abs center" style="left:150px;top:115px;width:36px">Lorem ipsum dolor sit amet.</div>
  <div class="tiny abs center" style="left:206px;top:80px;width:36px">Lorem ipsum dolor sit amet.</div>
  <div class="tiny abs center" style="left:262px;top:115px;width:36px">Lorem ipsum dolor sit amet.</div>
  <div class="foot"><span>© 2017 VELVET HARBOR. All rights reserved.</span><span>45</span></div>
</section>

<!-- 13 timeline -->
<section class="slide">
  <h2 class="title">TIMELINE</h2>
  <div class="brand"><i></i>VELVET HARBOR</div>
  <svg class="abs" style="left:0;top:0" width="337" height="189">
    <line x1="46" y1="89" x2="287" y2="89" stroke="#bbb" stroke-width=".8"/>
    <g stroke="#bbb" stroke-width=".6"><line x1="86" y1="70" x2="86" y2="89"/><line x1="127" y1="89" x2="127" y2="102"/><line x1="167" y1="70" x2="167" y2="89"/><line x1="207" y1="89" x2="207" y2="102"/><line x1="247" y1="70" x2="247" y2="89"/></g>
    <circle cx="46" cy="86" r="19" fill="#1c1c1c"/><circle cx="287" cy="86" r="19" fill="#1c1c1c"/>
    <circle cx="86" cy="54" r="16" fill="#f2d8cd"/><circle cx="247" cy="54" r="16" fill="#f2d8cd"/>
    <circle cx="127" cy="118" r="16" fill="#6b6b6b"/><circle cx="167" cy="54" r="16" fill="#6b6b6b"/><circle cx="207" cy="118" r="16" fill="#6b6b6b"/>
    <g font-size="8" text-anchor="middle">
      <text x="46" y="87" fill="#fff">2012</text><text x="287" y="87" fill="#fff">2018</text>
      <text x="86" y="55" fill="#777">2013</text><text x="247" y="55" fill="#777">2017</text>
      <text x="127" y="119" fill="#fff">2014</text><text x="167" y="55" fill="#fff">2015</text><text x="207" y="119" fill="#fff">2016</text>
    </g>
    <g font-size="2.6" text-anchor="middle">
      <text x="46" y="93" fill="#ccc">Your Text Goes Here</text><text x="287" y="93" fill="#ccc">Your Text Goes Here</text>
      <text x="86" y="60" fill="#999">Your Text Goes Here</text><text x="247" y="60" fill="#999">Your Text Goes Here</text>
      <text x="127" y="124" fill="#ddd">Your Text Goes Here</text><text x="167" y="60" fill="#ddd">Your Text Goes Here</text><text x="207" y="124" fill="#ddd">Your Text Goes Here</text>
    </g>
    <path d="M296,103 Q296,118 284,120" fill="none" stroke="#1c1c1c" stroke-width=".6"/>
  </svg>
  <div class="abs" style="left:238px;top:118px;width:80px;text-align:right"><div class="label">Your Text Goes Here</div><div class="tiny">Lorem ipsum dolor sit amet, consectetur adipiscing elit sed do eiusmod.</div></div>
  <div class="abs" style="left:14px;top:152px;width:150px"><div class="label">Your Text Goes Here</div><div class="tiny">Lorem ipsum dolor sit amet, consectetur adipiscing elit sed do eiusmod tempor incididunt.</div></div>
  <div class="foot"><span>© 2017 VELVET HARBOR. All rights reserved.</span><span>46</span></div>
</section>

<!-- 14 team -->
<section class="slide">
  <h2 class="title">OUR TEAM</h2>
  <div class="brand"><i></i>VELVET HARBOR</div>
  <div class="photo" style="left:20px;top:46px;width:38px;height:38px;border-radius:50%" role="img" aria-label="Portrait photo of team member"></div>
  <div class="photo" style="left:172px;top:46px;width:38px;height:38px;border-radius:50%" role="img" aria-label="Portrait photo of team member"></div>
  <div class="photo" style="left:20px;top:107px;width:38px;height:38px;border-radius:50%" role="img" aria-label="Portrait photo of team member"></div>
  <div class="photo" style="left:172px;top:107px;width:38px;height:38px;border-radius:50%" role="img" aria-label="Portrait photo of team member"></div>
  <div class="abs" style="left:64px;top:54px;width:90px"><div style="font-size:6.5px">Owen Marlow</div><div class="tiny" style="color:#555">CEO<br>MSMPT, MBA and CMA Dip PM</div><div class="tiny">• Lorem ipsum dolor sit amet, consectetur adipiscing elit<br>• Sed do eiusmod tempor incididunt ut labore<br>• Ut enim minim veniam</div></div>
  <div class="abs" style="left:212px;top:54px;width:90px"><div style="font-size:6.5px">Reid Calder</div><div class="tiny" style="color:#555">Manager<br>M.B.A</div><div class="tiny">• Lorem ipsum dolor sit amet, consectetur adipiscing elit<br>• Sed do eiusmod tempor incididunt ut labore<br>• Ut enim minim veniam</div></div>
  <div class="abs" style="left:64px;top:118px;width:90px"><div style="font-size:6.5px">Ivy Lorne</div><div class="tiny" style="color:#555">Doctor of Chemistry<br>M.B.A</div><div class="tiny">• Lorem ipsum dolor sit amet, consectetur adipiscing elit<br>• Sed do eiusmod tempor incididunt<br>• Ut enim minim veniam</div></div>
  <div class="abs" style="left:212px;top:118px;width:90px"><div style="font-size:6.5px">Neil Ashby</div><div class="tiny" style="color:#555">Doctor of Physical<br>Professor</div><div class="tiny">• Lorem ipsum dolor sit amet, consectetur adipiscing elit<br>• Sed do eiusmod tempor incididunt<br>• Ut enim minim veniam</div></div>
  <div class="foot"><span>© 2017 VELVET HARBOR. All rights reserved.</span><span>47</span></div>
</section>

<!-- 15 testimonials -->
<section class="slide">
  <h2 class="title">CUSTOMER TESTIMONIALS</h2>
  <div class="brand"><i></i>VELVET HARBOR</div>
  <div class="photo" style="left:72px;top:40px;width:46px;height:46px;border-radius:50%" role="img" aria-label="Portrait photo of a client"></div>
  <div class="tiny abs" style="left:145px;top:52px;width:160px">Adipiscing elit, sed diam nonummy nibh euismod tincidunt ut laoreet dolore magna aliquam erat volutpat. Ut wisi enim <span style="color:#333">Lorem ipsum</span> dolor sit amet, consectetur adipiscing elit, sed diam nonummy nibh euismod tincidunt ut laoreet dolore.</div>
  <div class="abs" style="left:0;right:0;top:100px;bottom:0;background:var(--ink)"></div>
  <svg class="abs" style="left:90px;top:96px" width="10" height="5"><path d="M0,4 L5,0 L10,4Z" fill="#1c1c1c"/></svg>
  <svg class="abs" style="left:0;top:100px" width="337" height="89">
    <g fill="none" stroke="#fff" stroke-width=".8"><circle cx="79" cy="31" r="13"/><circle cx="143" cy="31" r="13"/><circle cx="207" cy="31" r="13"/><circle cx="273" cy="31" r="13"/></g>
    <g fill="none" stroke="#fff" stroke-width=".7"><rect x="74" y="26" width="10" height="9"/><rect x="138" y="26" width="10" height="9"/><rect x="202" y="26" width="10" height="9"/><rect x="268" y="26" width="10" height="9"/></g>
  </svg>
  <div class="tiny abs center" style="left:56px;top:154px;width:46px;color:#ccc">Why does getting a loan have to be so complicated?</div>
  <div class="tiny abs center" style="left:120px;top:154px;width:46px;color:#ccc">Why do I have to go to a branch to get a response?</div>
  <div class="tiny abs center" style="left:184px;top:154px;width:46px;color:#ccc">Why do banks refuse to lend to me despite my record?</div>
  <div class="tiny abs center" style="left:250px;top:154px;width:46px;color:#ccc">Why is there no service that fits my needs and offers convenience?</div>
</section>

<!-- 16 bullet & chart -->
<section class="slide">
  <h2 class="title">BULLET &amp; CHART AREA</h2>
  <div class="brand"><i></i>VELVET HARBOR</div>
  <div class="item" style="left:38px;top:58px"><span class="dot" style="width:12px;height:12px;background:var(--ink)"></span><div><div class="label">Your Text Here</div><div class="tiny">Lorem ipsum dolor sit amet, consectetur<br>adipiscing elit, sed do eiusmod.</div></div></div>
  <div class="item" style="left:38px;top:85px"><span class="dot" style="width:12px;height:12px;background:var(--rose)"></span><div><div class="label" style="color:#e2bfb1">Your Text Here</div><div class="tiny">Lorem ipsum dolor sit amet, consectetur<br>adipiscing elit, sed do eiusmod.</div></div></div>
  <div class="item" style="left:38px;top:112px"><span class="dot" style="width:12px;height:12px;background:var(--grey)"></span><div><div class="label">Your Text Here</div><div class="tiny">Lorem ipsum dolor sit amet, consectetur<br>adipiscing elit, sed do eiusmod.</div></div></div>
  <div class="item" style="left:38px;top:140px"><span class="dot" style="width:12px;height:12px;background:var(--silver)"></span><div><div class="label">Your Text Here</div><div class="tiny">Lorem ipsum dolor sit amet, consectetur<br>adipiscing elit, sed do eiusmod.</div></div></div>
  <svg class="abs" style="left:0;top:0" width="337" height="189">
    <g transform="rotate(-90 244 106)" fill="none" stroke-width="10">
      <circle cx="244" cy="106" r="34" stroke="#1c1c1c" stroke-dasharray="128.2 213.6"/>
      <circle cx="244" cy="106" r="34" stroke="#f2d8cd" stroke-dasharray="53.4 213.6" stroke-dashoffset="-128.2"/>
      <circle cx="244" cy="106" r="34" stroke="#e4e4e4" stroke-dasharray="10.7 213.6" stroke-dashoffset="-181.6"/>
      <circle cx="244" cy="106" r="34" stroke="#8a8a8a" stroke-dasharray="21.3 213.6" stroke-dashoffset="-192.3"/>
    </g>
    <g fill="#8a8a8a"><rect x="234" y="108" width="3" height="6"/><rect x="239" y="104" width="3" height="10"/><rect x="244" y="100" width="3" height="14"/><rect x="249" y="96" width="3" height="18"/></g>
    <line x1="232" y1="115" x2="254" y2="115" stroke="#8a8a8a" stroke-width=".6"/>
    <g font-size="10"><text x="282" y="112" fill="#1c1c1c">60%</text><text x="184" y="86" fill="#777">15%</text><text x="216" y="64" fill="#999">10%</text><text x="184" y="134" fill="#f2d8cd">25%</text></g>
    <text x="208" y="158" font-size="3.5" fill="#999">● 1st Qtr  ● 2nd Qtr  ● 3rd Qtr  ● 4th Qtr</text>
  </svg>
  <div class="foot"><span>© 2017 VELVET HARBOR. All rights reserved.</span><span>49</span></div>
</section>

<!-- 17 contact -->
<section class="slide">
  <div class="dark-photo" role="img" aria-label="Dark monochrome photo of a building interior"></div>
  <div class="abs" style="left:34px;top:0;width:151px;bottom:0;background:var(--char)"></div>
  <div class="abs center" style="left:34px;top:14px;width:151px;color:#aaa;font-size:9px">
    <i class="dot" style="width:14px;height:14px;border:1px solid #aaa;display:block;margin:0 auto 3px"></i>VELVET HARBOR
  </div>
  <div class="abs" style="left:46px;top:64px;font-size:11px;color:#eee;border-bottom:.6px solid var(--rose);padding-bottom:3px">OUR CONTACT</div>
  <div class="abs" style="left:46px;top:94px;font-size:5px;color:#ddd;line-height:1.3">
    <div style="display:flex;gap:5px;margin-bottom:6px"><svg width="6" height="7"><path d="M3,7 C0,3.5 0,3 0,3 A3,3 0 0 1 6,3 C6,3 6,3.5 3,7Z" fill="#eee"/></svg><span>48 Quay Lane<br>Port 20418</span></div>
    <div style="display:flex;gap:5px;margin-bottom:7px"><svg width="6" height="6"><path d="M1,0 L2.5,0 L3,2 L2,3 Q3,4.5 4,4 L6,4.5 L6,6 Q1,6 0,1Z" fill="#eee"/></svg><span>(555) 201-3344</span></div>
    <div style="display:flex;gap:5px;margin-bottom:7px"><svg width="6" height="5"><rect width="6" height="5" fill="#eee"/><path d="M0,0 L3,2.5 L6,0" stroke="#2b2b2b" stroke-width=".6" fill="none"/></svg><span>hello@velvetharbor.co</span></div>
    <div style="display:flex;gap:5px"><svg width="6" height="6"><circle cx="3" cy="3" r="3" fill="#eee"/></svg><span>www.velvetharbor.co</span></div>
  </div>
  <div class="abs" style="left:34px;top:172px;width:151px;height:17px;background:var(--rose);display:flex;justify-content:center;align-items:center;gap:5px">
    <i class="dot" style="width:7px;height:7px;background:#fff"></i><i class="dot" style="width:7px;height:7px;background:#fff"></i><i class="dot" style="width:7px;height:7px;background:#fff"></i>
  </div>
  <div class="abs center" style="left:190px;top:108px;width:140px;color:#fff">
    <div style="font-size:14px">THANK YOU</div>
    <div style="font-size:5.5px;color:#ccc;margin-bottom:6px">For Your Precious Time</div>
    <div style="font-size:4.5px;color:#ccc;line-height:1.5">Stop by our office or give us a call!<br>We would love to hear from you.</div>
  </div>
</section>

<!-- 18 closing -->
<section class="slide" style="background:var(--ink)">
  <div class="abs center" style="left:0;right:0;top:30px;color:#9a9a9a">
    <i class="dot" style="width:30px;height:30px;border:1.2px solid #9a9a9a;display:block;margin:0 auto 8px"></i>
    <div style="font-size:17px;letter-spacing:.5px">VELVET HARBOR</div>
    <div style="font-size:14px;color:#eee;margin-top:26px">THANK YOU</div>
    <div style="font-size:5.5px;color:#bbb">For Your Precious Time</div>
  </div>
</section>

</main>
</body>
</html>
```